Brightvale Wound Care
Business cards and letterhead
Professional
Gregory Tamsett
Chief Executive Officer
3470 P Street NW
Suite 615
Washington, DC 20011
gtamsett@brightvale-wc.example
www.brightvale-wc.example
I need one that says "CEO" for the name above and one that says "Territory Manager". I also need (with the same design for the name Darren Pulcombe as "President" and one for him as well that says Senior Territory Manager"
I need to list these products on the back:
1. Verashu Negitive Pressure Wound Therapy
2. Brunix Negitive Pressure Wound Therapy
3. Orvil alternating pressure mattresses
Here is our logo please use this logo while doing our design for this project for both the business cards and letterhead. Thanks
Please add this one or the non-green one (also uploaded) some where on the card. Make it very small please.
Or add this one to the card somewhere. Whatever one looks better.

```html
<!DOCTYPE html>
<html lang="en">
<head>
<meta charset="utf-8">
<title>Brightvale Wound Care — Stationery</title>
<link rel="stylesheet" href="https://fonts.googleapis.com/css2?family=Montserrat:wght@400;500;600&display=swap">
<style>
  :root {
    --brand-red: #e3192f;
    --brand-blue: #3b2c98;
    --brand-mid: #8a2466;
    --ink: #2f2c6e;
    --text-grey: #6d6d78;
    --paper: #ffffff;
    --backdrop: #ffffff;
    --edge: #dcdce2;
    --rule: #f0a7ae;
    --grad: linear-gradient(90deg, var(--brand-red) 0%, var(--brand-mid) 55%, var(--brand-blue) 100%);
  }
  * { box-sizing: border-box; margin: 0; padding: 0; }
  html, body { width: 1200px; height: 806px; overflow: hidden; background: var(--backdrop); }
  body { font-family: "Montserrat", sans-serif; color: var(--ink); position: relative; }

  .sheet { position: absolute; background: var(--paper); border: 1px solid var(--edge); box-shadow: 0 1px 3px rgba(0,0,0,.08); overflow: hidden; }

  /* brand name lockup */
  .brand { display: flex; align-items: center; gap: 6px; white-space: nowrap; }
  .brand__dot { width: 12px; height: 12px; border-radius: 50%; background: var(--brand-red); flex: none; }
  .brand__name { font-weight: 500; color: var(--ink); font-size: 11px; letter-spacing: -.1px; }
  .brand__rule { flex: 1; height: 1px; background: var(--rule); margin-left: 6px; }

  /* business card front */
  .card { width: 172px; height: 98px; }
  .card-front { padding: 8px 9px; }
  .card-front .person { text-align: right; }
  .card-front .person__name { font-size: 8px; font-weight: 600; color: var(--brand-blue); }
  .card-front .person__title { font-size: 5.5px; color: var(--text-grey); margin-top: 1px; }
  .card-front .brand { position: absolute; left: 9px; right: 9px; top: 42px; }
  .card-front .brand__name { font-size: 9px; }
  .card-front .brand__dot { width: 9px; height: 9px; }
  .card-front .details { position: absolute; left: 9px; bottom: 8px; font-size: 4.6px; line-height: 1.45; color: var(--text-grey); }

  /* business card back */
  .card-back { background: var(--grad); border: none; color: #fff; }
  .card-back .symbol { position: absolute; width: 26px; height: 26px; border: 2px solid rgba(255,255,255,.9); border-radius: 50%; }
  .card-back .products { position: absolute; font-size: 5.4px; line-height: 1.6; }
  .card-back .products__head { font-weight: 600; font-size: 6px; }
  .card-back--side .symbol { left: 22px; top: 36px; }
  .card-back--side .products { left: 68px; top: 34px; }
  .card-back--top .symbol { left: 73px; top: 12px; }
  .card-back--top .products { left: 0; right: 0; top: 48px; text-align: center; }

  .side-label { position: absolute; font-size: 6px; color: var(--text-grey); }

  /* envelope */
  .envelope { left: 32px; top: 410px; width: 560px; height: 262px; }
  .envelope__flap { position: absolute; left: 0; top: 0; width: 100%; height: 112px; display: block; }
  .envelope .brand { position: absolute; left: 22px; right: 22px; top: 136px; }
  .envelope .brand__name { font-size: 17px; }
  .envelope .brand__dot { width: 16px; height: 16px; }
  .envelope__return { position: absolute; left: 22px; bottom: 16px; font-size: 7px; color: var(--text-grey); }

  /* letterhead */
  .letterhead { left: 618px; top: 28px; width: 562px; height: 750px; }
  .letterhead .brand { position: absolute; left: 34px; right: 34px; top: 40px; }
  .letterhead .brand__name { font-size: 19px; }
  .letterhead .brand__dot { width: 18px; height: 18px; }
  .letterhead__decor { position: absolute; right: 42px; top: 250px; width: 240px; height: 240px; border-radius: 50%; border: 14px solid rgba(150,80,150,.09); }
  .letterhead__footer { position: absolute; left: 34px; right: 34px; bottom: 26px; border-top: 1px solid var(--rule); padding-top: 6px; font-size: 6.6px; line-height: 1.6; color: var(--text-grey); }
  .letterhead__footer b { color: var(--brand-red); font-weight: 600; }
</style>
</head>
<body>

  <!-- Row 1: CEO card, President card, back -->
  <section class="sheet card card-front" style="left:32px; top:40px;">
    <div class="person"><p class="person__name">Gregory Tamsett</p><p class="person__title">Chief Executive Officer</p></div>
    <div class="brand"><span class="brand__dot"></span><span class="brand__name">Brightvale Wound Care</span><span class="brand__rule"></span></div>
    <p class="details">3470 P Street NW Suite 615 Washington, DC 20011<br>P: 202.555.0148 E: gtamsett@brightvale-wc.example<br>www.brightvale-wc.example</p>
  </section>

  <section class="sheet card card-front" style="left:222px; top:40px;">
    <div class="person"><p class="person__name">Darren Pulcombe</p><p class="person__title">President</p></div>
    <div class="brand"><span class="brand__dot"></span><span class="brand__name">Brightvale Wound Care</span><span class="brand__rule"></span></div>
    <p class="details">3470 P Street NW Suite 615 Washington, DC 20011<br>P: 202.555.0148 F: 202.555.0149<br>www.brightvale-wc.example</p>
  </section>

  <section class="sheet card card-back card-back--side" style="left:412px; top:40px;">
    <span class="symbol"></span>
    <div class="products">
      <p class="products__head">Our Products</p>
      <p>Verashu Negative Pressure Wound Therapy</p>
      <p>Brunix Negative Pressure Wound Therapy</p>
      <p>Orvil Alternating Pressure Mattresses</p>
    </div>
  </section>
  <span class="side-label" style="left:590px; top:86px;">Back</span>

  <!-- Row 2: CEO card, Senior Territory Manager card, back -->
  <section class="sheet card card-front" style="left:32px; top:150px;">
    <div class="person"><p class="person__name">Gregory Tamsett</p><p class="person__title">CEO</p></div>
    <div class="brand"><span class="brand__dot"></span><span class="brand__name">Brightvale Wound Care</span><span class="brand__rule"></span></div>
    <p class="details">3470 P Street NW Suite 615 Washington, DC 20011<br>P: 202.555.0148 E: gtamsett@brightvale-wc.example<br>www.brightvale-wc.example</p>
  </section>

  <section class="sheet card card-front" style="left:222px; top:150px;">
    <div class="person"><p class="person__name">Darren Pulcombe</p><p class="person__title">Senior Territory Manager</p></div>
    <div class="brand"><span class="brand__dot"></span><span class="brand__name">Brightvale Wound Care</span><span class="brand__rule"></span></div>
    <p class="details">3470 P Street NW Suite 615 Washington, DC 20011<br>P: 202.555.0148 F: 202.555.0149<br>www.brightvale-wc.example</p>
  </section>

  <section class="sheet card card-back card-back--top" style="left:412px; top:150px;">
    <span class="symbol"></span>
    <div class="products">
      <p class="products__head">Our Products</p>
      <p>Verashu Negative Pressure Wound Therapy</p>
      <p>Brunix Negative Pressure Wound Therapy</p>
      <p>Orvil Alternating Pressure Mattresses</p>
    </div>
  </section>
  <span class="side-label" style="left:590px; top:196px;">Back</span>

  <!-- Envelope -->
  <section class="sheet envelope">
    <svg class="envelope__flap" viewBox="0 0 560 112" preserveAspectRatio="none" aria-hidden="true">
      <defs>
        <linearGradient id="flapGrad" x1="0" y1="0" x2="1" y2="0">
          <stop offset="0" stop-color="#e3192f"/>
          <stop offset=".55" stop-color="#8a2466"/>
          <stop offset="1" stop-color="#3b2c98"/>
        </linearGradient>
      </defs>
      <path d="M0 0 H560 L300 104 Q280 112 260 104 Z" fill="url(#flapGrad)"/>
      <circle cx="280" cy="38" r="13" fill="none" stroke="#ffffff" stroke-width="2.4"/>
    </svg>
    <div class="brand"><span class="brand__dot"></span><span class="brand__name">Brightvale Wound Care</span><span class="brand__rule"></span></div>
    <p class="envelope__return">3470 P Street NW Suite 615 Washington, DC 20011</p>
  </section>

  <!-- Letterhead -->
  <section class="sheet letterhead">
    <div class="brand"><span class="brand__dot"></span><span class="brand__name">Brightvale Wound Care</span><span class="brand__rule"></span></div>
    <span class="letterhead__decor" aria-hidden="true"></span>
    <p class="letterhead__footer">3470 P Street NW Suite 615 Washington, DC 20011<br><b>P:</b> 202.555.0148 &nbsp;<b>F:</b> 202.555.0149 &nbsp;<b>E:</b> info@brightvale-wc.example &nbsp;<b>W:</b> www.brightvale-wc.example</p>
  </section>

</body>
</html>
```